Kovix Tralo Mart Listing Screenshot Design

We would like to create new screenshots for our Kovix app in the Tralo Mart to A/B test against the current version.

You can view our current Kovix Tralo Mart listing here: https://apps.tralomart.example/listing?id=com.quorvantic.kovix&hl=en

Attached I have added screenshots of the app that I would like to be included. Please edit the screenshots to generic text (e.g. John Smith, 123 Main St, etc.).

You can use the same text we have in the current ones. For text for the criminal screenshot please view our Zyn Zeph Shop listing: https://apps.zephshop.example/us/app/quorvantic-background-check/id907164352?mt=8

If you want to come up with new text please feel free to!

I also attached a few examples of other app screenshots that we like.

Kovix TraloMart Listing Guidelines: https://help.tralomart.example/tralomart/kovix-developer/answer/5526193?hl=en

Industry/Entity Type

Store

Font styles to use
Sans Serif

Colors
f0f0f0

Requirements
Must have
• ~Generic names and data like "John Smith", "54 Main St. Springfield, NJ 09876"
• ~Screenshot for Person Search, Criminal Records, Phone Search, Email Search, and Property Search. In that order.
• ~Headlines either the ones used in our current screenshots (https://apps.tralomart.example/listing?id=com.quorvantic.kovix&hl=en) or new ones you come up with.
• ~Must meet Kovix screenshot guidelines.
• ~Optimized for downloads.
• Must use following color palette:
• Dark purple #3B2469
• Light purple #7E6F9C
• Very dark gray #333333
• Dark gray #666666
• Gray #999999
• Blue gray #CFD9DE
• Green #5CB85C
• Navy #003577
• Yellow #F3B607
• Magenta #F0386B

```html
<!DOCTYPE html>
<html lang="en">
<head>
<meta charset="utf-8">
<title>Kovix – Criminal Records Listing Screenshot</title>
<link href="https://fonts.googleapis.com/css2?family=Open+Sans:wght@400;600&family=Roboto:wght@400;500&display=swap" rel="stylesheet">
<style>
  :root{
    --canvas:#f0f0f0;
    --magenta:#f0386b;
    --app-purple:#4a2e80;
    --tab-purple:#553a8c;
    --band-purple:#45297a;
    --label-gray:#999999;
    --value-dark:#333333;
    --white:#ffffff;
  }
  *{margin:0;padding:0;box-sizing:border-box}
  html,body{width:1200px;height:2511px;overflow:hidden;background:var(--canvas)}
  .listing-shot{position:relative;width:1200px;height:2511px;overflow:hidden;background:var(--canvas)}

  .headline-bar{position:absolute;left:0;top:0;width:1200px;height:224px;background:var(--magenta);
    display:flex;flex-direction:column;justify-content:center;align-items:center;text-align:center;
    font-family:"Open Sans",sans-serif;font-weight:600;color:var(--white);font-size:54px;letter-spacing:3px;line-height:78px}
  .headline-line{display:block;white-space:nowrap}

  .app-screen{position:absolute;left:118px;top:453px;width:920px;height:1622px;overflow:hidden;background:var(--white);
    font-family:"Roboto",sans-serif;box-shadow:0 4px 24px rgba(0,0,0,.08)}
  .status-bar{height:61px;background:var(--app-purple);display:flex;align-items:center;justify-content:space-between;padding:0 22px;color:var(--white);font-size:36px}
  .status-left,.status-right{display:flex;align-items:center;gap:20px}
  .app-bar{height:146px;background:var(--app-purple);display:flex;align-items:center;padding:0 40px;color:var(--white)}
  .app-title{font-size:56px;font-weight:500;letter-spacing:3px;margin-left:58px;flex:1;white-space:nowrap}
  .app-actions{display:flex;gap:44px;align-items:center}
  .tab-bar{position:relative;height:123px;background:var(--tab-purple);color:rgba(255,255,255,.55);font-size:34px;font-weight:500;white-space:nowrap}
  .tab{position:absolute;top:0;height:123px;display:flex;align-items:center}
  .tab--active{color:var(--white)}
  .tab-indicator{position:absolute;left:174px;bottom:0;width:571px;height:6px;background:var(--white)}

  .record-list{padding:0 17px}
  .record-field{height:151px;padding-top:16px}
  .field-label{font-size:38px;font-weight:500;color:var(--label-gray);line-height:48px;white-space:nowrap}
  .field-value{font-size:40px;color:var(--value-dark);line-height:52px;margin-top:16px;white-space:nowrap}

  .feature-band{position:absolute;left:0;top:1573px;width:1200px;height:247px;background:var(--band-purple);opacity:.93;
    display:flex;align-items:center;justify-content:center;white-space:nowrap;
    font-family:"Open Sans",sans-serif;font-weight:400;font-size:100px;letter-spacing:4px;color:var(--white)}
  .band-glow{position:absolute;left:118px;width:920px;height:80px}
  .band-glow--top{top:1493px;background:linear-gradient(to bottom,rgba(255,255,255,0),rgba(255,255,255,.85))}
  .band-glow--bottom{top:1820px;background:linear-gradient(to top,rgba(255,255,255,0),rgba(255,255,255,.85))}
</style>
</head>
<body>
<main class="listing-shot">
  <header class="headline-bar">
    <span class="headline-line">FIND SHOCKING INFORMATION</span>
    <span class="headline-line">LIKE CRIMINAL &amp; TRAFFIC RECORDS</span>
  </header>

  <section class="app-screen">
    <div class="status-bar">
      <div class="status-left">
        <svg width="30" height="30" viewBox="0 0 30 30"><rect x="2" y="3" width="26" height="24" fill="none" stroke="#fff" stroke-width="3"/><path d="M6 23l6-8 5 6 4-4 4 6z" fill="#fff"/></svg>
        <svg width="32" height="26" viewBox="0 0 32 26"><rect x="2" y="2" width="28" height="22" fill="#fff"/><path d="M5 6l11 9 11-9" fill="none" stroke="#4a2e80" stroke-width="3"/></svg>
        <svg width="26" height="30" viewBox="0 0 26 30"><rect x="2" y="2" width="22" height="26" fill="#fff"/><path d="M8 10l10 10M18 10L8 20" stroke="#d9363e" stroke-width="3"/></svg>
      </div>
      <div class="status-right">
        <svg width="34" height="32" viewBox="0 0 34 32"><path d="M4 12h6l8-7v22l-8-7H4z" fill="#fff"/><path d="M22 11l9 10M31 11l-9 10" stroke="#fff" stroke-width="3"/></svg>
        <svg width="40" height="32" viewBox="0 0 40 32"><path d="M2 10a26 26 0 0136 0M8 17a17 17 0 0124 0M14 24a8 8 0 0112 0" fill="none" stroke="#fff" stroke-width="3.5"/><circle cx="20" cy="29" r="3" fill="#fff"/></svg>
        <svg width="36" height="34" viewBox="0 0 36 34"><path d="M34 2v30H2z" fill="#fff"/></svg>
        <span>18%</span>
        <svg width="20" height="36" viewBox="0 0 20 36"><rect x="2" y="5" width="16" height="29" fill="none" stroke="#fff" stroke-width="3"/><rect x="6" y="1" width="8" height="4" fill="#fff"/><rect x="4" y="26" width="12" height="7" fill="#fff"/></svg>
        <span>5:08 PM</span>
      </div>
    </div>
    <div class="app-bar">
      <svg width="48" height="48" viewBox="0 0 48 48"><path d="M42 24H8M22 10L8 24l14 14" fill="none" stroke="#fff" stroke-width="4.5"/></svg>
      <span class="app-title">MATH SMITH</span>
      <div class="app-actions">
        <svg width="56" height="56" viewBox="0 0 56 56"><path d="M28 6a4 4 0 014 4v2c8 2 12 8 12 16v10l5 5v2H7v-2l5-5V28c0-8 4-14 12-16v-2a4 4 0 014-4zM22 47h12a6 6 0 01-12 0z" fill="#fff"/></svg>
        <svg width="52" height="52" viewBox="0 0 52 52"><circle cx="26" cy="26" r="22" fill="none" stroke="#fff" stroke-width="4"/><path d="M19 20a7 7 0 1110 6c-2 1-3 3-3 6" fill="none" stroke="#fff" stroke-width="4"/><circle cx="26" cy="39" r="2.8" fill="#fff"/></svg>
        <svg width="14" height="52" viewBox="0 0 14 52"><circle cx="7" cy="8" r="5" fill="#fff"/><circle cx="7" cy="26" r="5" fill="#fff"/><circle cx="7" cy="44" r="5" fill="#fff"/></svg>
      </div>
    </div>
    <nav class="tab-bar">
      <span class="tab" style="left:4px">GHBORS</span>
      <span class="tab tab--active" style="left:205px">CRIMINAL &amp; TRAFFIC RECORDS</span>
      <span class="tab" style="left:778px">BANKRU</span>
      <span class="tab-indicator"></span>
    </nav>
    <div class="record-list">
      <div class="record-field"><p class="field-label">OFFENSE DATE</p><p class="field-value">Feb 24, 2009</p></div>
      <div class="record-field"><p class="field-label">DESCRIPTION OF OFFENSE</p><p class="field-value">AGGRAVATED ASSAULT, ATTEMPT TO COMMIT</p></div>
      <div class="record-field"><p class="field-label">OFFENSE TYPE</p><p class="field-value">Department Of Correction</p></div>
      <div class="record-field"><p class="field-label">CASE NUMBER</p><p class="field-value">N/A</p></div>
      <div class="record-field"><p class="field-label">AGENCY</p><p class="field-value">N/A</p></div>
      <div class="record-field"><p class="field-label">DATE</p><p class="field-value">N/A</p></div>
      <div class="record-field"><p class="field-label">&nbsp;</p><p class="field-value">AGGRAVATED ASSAULT, ATTEMPT TO COMMIT</p></div>
      <div class="record-field"><p class="field-label">DISPOSITION</p><p class="field-value">N/A</p></div>
      <div class="record-field"><p class="field-label">LEVEL</p><p class="field-value">F</p></div>
    </div>
  </section>

  <div class="band-glow band-glow--top"></div>
  <div class="band-glow band-glow--bottom"></div>
  <div class="feature-band">CRIMINAL RECORDS</div>
</main>
</body>
</html>
```